Harbor Crestline (Business Card Design)

Need business cards designed. Something modern, chic, and sleek. Mabye the back of the card should be the navy blue that is in the logo and then just the logo on the back.

Target Market(s)

Those in the hotel, office, and renovation industry

Contact Information for Business Card

1. Logo 2. Tomasz Ferreiro 3. CEO/Founder 4. Phone: (833) HarbCre / (833) 427-2273 5. Email: tomasz@theharborcrestline.com 6. Website: www.theharborcrestline.com

Font styles to use
Other font styles liked:
• Look at the logo font and base the font for everything else off of that.

Colors
0054AA
0677BA
7BADD7
CADEEF
E8F1F8

Requirements
Must have
• Colors that are associated in the logo
Nice to have
• Sleek modern clean and chic design.

```html
<!DOCTYPE html>
<html lang="en">
<head>
<meta charset="utf-8">
<title>Harbor Crestline — Business Card</title>
<link rel="stylesheet" href="https://fonts.googleapis.com/css2?family=Montserrat:wght@400;500;600&display=swap">
<style>
  :root {
    --navy: #0d1a40;
    --navy-deep: #0b1638;
    --gold: #c9a44a;
    --white: #ffffff;
    --ink: #3b3b3b;
    --stage-dark: #333333;
    --stage-light: #ffffff;
  }
  * { margin: 0; padding: 0; box-sizing: border-box; }
  html, body { width: 1200px; height: 2887px; overflow: hidden; }
  body { font-family: "Montserrat", sans-serif; }

  .stage { position: relative; width: 1200px; }
  .stage--dark { height: 1440px; background: var(--stage-dark); }
  .stage--light { height: 1447px; background: var(--stage-light); }

  .card {
    position: absolute;
    left: 43px;
    width: 1114px;
    height: 567px;
    overflow: hidden;
  }
  .stage--dark .card { box-shadow: 0 26px 28px -14px rgba(0,0,0,0.75); }
  .stage--light .card { box-shadow: 0 6px 22px rgba(0,0,0,0.28); }

  .card--front { top: 78px; background: radial-gradient(ellipse at center, #0e1c45 0%, var(--navy) 70%); }
  .card--back  { top: 726px; background: var(--white); }
  .stage--light .card--front { top: 81px; }
  .stage--light .card--back  { top: 729px; }

  /* Front */
  .front-mark {
    position: absolute; left: 0; right: 0; top: 205px;
    display: flex; flex-direction: column; align-items: center;
  }
  .front-mark__square { width: 22px; height: 22px; background: var(--gold); margin-bottom: 42px; }
  .front-mark__name {
    color: var(--white); font-weight: 600; font-size: 50px;
    letter-spacing: 5px; text-align: center; line-height: 1.15;
  }

  /* Back */
  .back-header { position: absolute; left: 0; top: 0; width: 1114px; height: 223px; background: var(--navy); }
  .back-header svg { position: absolute; inset: 0; }
  .back-brand {
    position: absolute; left: 120px; top: 62px; width: 230px;
    display: flex; flex-direction: column; align-items: center;
  }
  .back-brand__square { width: 16px; height: 16px; background: var(--gold); margin-bottom: 22px; }
  .back-brand__name {
    color: var(--white); font-weight: 600; font-size: 27px;
    letter-spacing: 2px; text-align: center; line-height: 1.15;
  }
  .person { position: absolute; left: 718px; top: 62px; color: var(--white); }
  .person__name { font-weight: 600; font-size: 47px; line-height: 1.1; }
  .person__role { font-weight: 400; font-size: 27px; margin-top: 2px; }

  .contact { position: absolute; left: 180px; top: 278px; }
  .contact__row { display: flex; align-items: center; height: 60px; color: var(--ink); }
  .contact__row--phone { font-size: 38px; font-weight: 500; }
  .contact__row--email { font-size: 33px; font-weight: 500; }
  .contact__icon { width: 36px; height: 36px; margin-right: 20px; flex: none; }

  .back-footer {
    position: absolute; left: 0; bottom: 0; width: 1114px; height: 127px;
    background: var(--navy-deep);
    display: flex; align-items: center; justify-content: center;
    color: var(--white); font-size: 30px; font-weight: 500; letter-spacing: 2.5px;
  }
  .back-footer__domain { color: var(--gold); }
</style>
</head>
<body>

<section class="stage stage--dark">
  <article class="card card--front">
    <div class="front-mark">
      <span class="front-mark__square"></span>
      <p class="front-mark__name">HARBOR CRESTLINE</p>
    </div>
  </article>

  <article class="card card--back">
    <header class="back-header">
      <svg width="1114" height="223" viewBox="0 0 1114 223">
        <polygon points="600,0 1114,0 1114,223 580,223 690,103" fill="var(--gold)"/>
      </svg>
      <div class="back-brand">
        <span class="back-brand__square"></span>
        <p class="back-brand__name">HARBOR<br>CRESTLINE</p>
      </div>
      <div class="person">
        <p class="person__name">Tomasz Ferreiro</p>
        <p class="person__role">CEO/Founder</p>
      </div>
    </header>
    <div class="contact">
      <p class="contact__row contact__row--phone">
        <svg class="contact__icon" viewBox="0 0 36 36"><circle cx="18" cy="18" r="16" fill="none" stroke="var(--gold)" stroke-width="2"/><path d="M12 10c1-1 2-1 3 0l2 3c.5 1 0 2-1 2.5 1 2.5 3 4.5 5.5 5.5.5-1 1.5-1.5 2.5-1l3 2c1 1 1 2 0 3-2 2-5 2-9-1.5S10 14 12 10z" fill="none" stroke="var(--navy)" stroke-width="1.6"/></svg>
        (833) HarbCre / (833) 427-2273
      </p>
      <p class="contact__row contact__row--email">
        <svg class="contact__icon" viewBox="0 0 36 36"><circle cx="18" cy="18" r="16" fill="none" stroke="var(--gold)" stroke-width="2"/><rect x="11" y="13" width="14" height="10" fill="none" stroke="var(--navy)" stroke-width="1.6"/><path d="M11 13l7 6 7-6" fill="none" stroke="var(--navy)" stroke-width="1.6"/></svg>
        tomasz@theharborcrestline.com
      </p>
    </div>
    <footer class="back-footer">
      <span>www.</span><span class="back-footer__domain">theharborcrestline</span><span>.com</span>
    </footer>
  </article>
</section>

<section class="stage stage--light">
  <article class="card card--front">
    <div class="front-mark">
      <span class="front-mark__square"></span>
      <p class="front-mark__name">HARBOR CRESTLINE</p>
    </div>
  </article>

  <article class="card card--back">
    <header class="back-header">
      <svg width="1114" height="223" viewBox="0 0 1114 223">
        <polygon points="600,0 1114,0 1114,223 580,223 690,103" fill="var(--gold)"/>
      </svg>
      <div class="back-brand">
        <span class="back-brand__square"></span>
        <p class="back-brand__name">HARBOR<br>CRESTLINE</p>
      </div>
      <div class="person">
        <p class="person__name">Tomasz Ferreiro</p>
        <p class="person__role">CEO/Founder</p>
      </div>
    </header>
    <div class="contact">
      <p class="contact__row contact__row--phone">
        <svg class="contact__icon" viewBox="0 0 36 36"><circle cx="18" cy="18" r="16" fill="none" stroke="var(--gold)" stroke-width="2"/><path d="M12 10c1-1 2-1 3 0l2 3c.5 1 0 2-1 2.5 1 2.5 3 4.5 5.5 5.5.5-1 1.5-1.5 2.5-1l3 2c1 1 1 2 0 3-2 2-5 2-9-1.5S10 14 12 10z" fill="none" stroke="var(--navy)" stroke-width="1.6"/></svg>
        (833) HarbCre / (833) 427-2273
      </p>
      <p class="contact__row contact__row--email">
        <svg class="contact__icon" viewBox="0 0 36 36"><circle cx="18" cy="18" r="16" fill="none" stroke="var(--gold)" stroke-width="2"/><rect x="11" y="13" width="14" height="10" fill="none" stroke="var(--navy)" stroke-width="1.6"/><path d="M11 13l7 6 7-6" fill="none" stroke="var(--navy)" stroke-width="1.6"/></svg>
        tomasz@theharborcrestline.com
      </p>
    </div>
    <footer class="back-footer">
      <span>www.</span><span class="back-footer__domain">theharborcrestline</span><span>.com</span>
    </footer>
  </article>
</section>

</body>
</html>
```